Zielgruppe
Wir sind ein Business Center und vermieten Büro- und Konferenzräume. Wir richten uns an Unternehmen unterschiedlichster Branchen: Freelancer ohne eigenes Büro oder auch große Unternehmen, welche keine eigene freien Vakanzen haben, z. B. für Vorstellungsgespräche.
Aufgabenstellung
Flyer Din Lang, quer, gebunden an der kurzen Seite. 8 Seiten, inkl. Vorder- und Rückseite. Bitte kein Wickelfalz oder ähnliches, sondern eine Broschüre, gebunden mit Klammerheftung!!!
Frisches helles Design, ohne Schnörkel. Bilder mit etwas Text, dazu eine Seite über uns. Rückseite Kontaktdaten. Je eine Doppelseite für Konferenzraumvermietung und eine Doppelseite für Büroraum auf Zeit, eine Doppelseite für unsere weitere Leistungen, Telefonservice (Anrufannahme im namen unserer Kunden).
Unsere Räume sind sehr repräsentativ und modern eingerichtet mit hellen Designermöbeln. Das soll auch in der Broschüre klar werden.

```html
<!DOCTYPE html>
<html lang="de">
<head>
<meta charset="utf-8">
<title>Velburo – Flyer Außenseiten</title>
<link href="https://fonts.googleapis.com/css2?family=Barlow:wght@400;600&family=Barlow+Semi+Condensed:wght@400&display=swap" rel="stylesheet">
<style>
  :root {
    --lime: #c8d623;
    --ink: #33352c;
    --paper: #ffffff;
    --frame: #1f1f1f;
  }
  * { margin: 0; padding: 0; box-sizing: border-box; }
  html, body { width: 1200px; height: 280px; overflow: hidden; background: var(--paper); }
  .spread {
    position: relative; width: 1200px; height: 280px;
    font-family: "Barlow", sans-serif; color: var(--ink);
    border: 1px solid var(--frame); overflow: hidden;
  }
  /* Rückseite */
  .about {
    position: absolute; left: 14px; top: 14px; width: 572px; height: 157px;
    background: var(--lime); padding: 14px 0 0 15px;
  }
  .about-title { font-size: 11px; font-weight: 600; letter-spacing: .2px; margin-bottom: 4px; }
  .about-columns { display: flex; gap: 14px; }
  .about-columns p { width: 200px; font-size: 9.2px; line-height: 12.1px; letter-spacing: .15px; }
  .about-columns .col-b { margin-top: -2px; }
  .about-columns .col-b p + p { margin-top: 12px; }
  .contact {
    position: absolute; left: 23px; top: 201px;
    font-size: 11px; line-height: 14px; letter-spacing: .4px; color: #111;
  }
  .contact-title { font-weight: 600; letter-spacing: .8px; }
  .online {
    position: absolute; left: 200px; top: 227px;
    font-size: 11px; line-height: 14px; letter-spacing: .3px; color: #111;
  }
  .brand {
    position: absolute; display: flex; align-items: center; gap: 6px;
    font-family: "Barlow", sans-serif; font-weight: 600; font-size: 21px;
    letter-spacing: .5px; color: var(--ink);
  }
  .brand-mark { width: 11px; height: 11px; background: var(--lime); }
  .brand--back { left: 455px; top: 218px; }
  /* Titelseite */
  .cover-photo { position: absolute; left: 600px; top: 0; width: 600px; height: 280px; }
  .cover-band {
    position: absolute; left: 600px; top: 180px; width: 600px; height: 71px;
    background: var(--lime);
  }
  .cover-title {
    position: absolute; left: 618px; top: 198px;
    font-family: "Barlow Semi Condensed", sans-serif; font-size: 30px;
    letter-spacing: 1.2px; color: var(--paper); line-height: 34px;
  }
  .cover-badge {
    position: absolute; left: 957px; top: 180px; width: 149px; height: 71px;
    background: var(--paper);
  }
  .brand--front { left: 974px; top: 201px; font-size: 20px; }
</style>
</head>
<body>
<div class="spread">
  <section class="about">
    <h2 class="about-title">WIR ÜBER UNS</h2>
    <div class="about-columns">
      <p>Lorem ipsum dolor sit amet, consectetuer adipiscing elit. Aenean commodo ligula eget dolor. Aenean massa. Cum sociis natoque penatibus et magnis dis parturient montes, nascetur ridiculus mus. Donec quam felis, ultricies nec, pellentesque eu, pretium quis, sem.&nbsp; Kest est durum feret elem.</p>
      <div class="col-b">
        <p>consequat massa quis enim. Donec pede jus­to, fringilla vel, aliquet nec, vulputate eget, arcu. In enim justo, rhoncus ut, imperdiet a, venenatis vitae, justo.</p>
        <p>Aenean massa. Cum sociis natoque penati­bus et magnis dis parturient montes, nasce</p>
      </div>
    </div>
  </section>

  <address class="contact" style="font-style:normal">
    <div class="contact-title">KONTAKT</div>
    <div>Harnweg Allee 212-220</div>
    <div>40110 Dalstedt</div>
    <div>0800 - 5 222 000</div>
  </address>
  <div class="online">
    <div>info@velburo.de</div>
    <div>www.telefonservice-velburo.de</div>
  </div>
  <div class="brand brand--back"><span class="brand-mark"></span>VELBURO</div>

  <svg class="cover-photo" role="img" aria-label="Foto eines hellen Konferenzraums mit weißem Tisch, grauen und cognacfarbenen Designerstühlen" viewBox="0 0 600 280" preserveAspectRatio="none">
    <defs>
      <linearGradient id="room" x1="0" y1="0" x2="0" y2="1">
        <stop offset="0" stop-color="#eceae6"/>
        <stop offset=".45" stop-color="#f4f3f1"/>
        <stop offset=".7" stop-color="#b9a38e"/>
        <stop offset="1" stop-color="#9a6a48"/>
      </linearGradient>
    </defs>
    <rect width="600" height="280" fill="url(#room)"/>
  </svg>
  <div class="cover-band"></div>
  <h1 class="cover-title">IHR (OUT OF) HOMEOFFICE</h1>
  <div class="cover-badge"></div>
  <div class="brand brand--front"><span class="brand-mark"></span>VELBURO</div>
</div>
</body>
</html>
```